Business card design needed

We need a business card design for a new consulting business based in Melbourne called Harbor Ridge Advisory. Our tag line is 'Creating Impact Together'. We work with not for profits and Small - Medium Enterprises to provide advice and solutions around finance, governance, HR, IT and risk management. The idea around our organisation is to help charities and small businesses with their business foundations, so that they can spend more time focussing on their mission.
We have a logo designed already and would like the business card to use similar colours and themes - collaboration, having a conversation, creating impact. We would like the design to be eye catching but also convey professional credibility.
We would like a double sided card please.
Target Market(s)
CEOs and senior managers in charities and Small to Medium Enterprises
Industry/Entity Type
Business
Contact Information for Business Card
Business Name: Harbor Ridge Advisory
Staff Member: Janet Colby FCA
Title: Principal Consultant
Email address: janet@harborridgeadvisory.com.au
Phone: 03 9871 2264
Mobile: 0412 846 309
Address: PO Box 87, Larkfield VIC 3148
Web: www.harborridgeadvisory.com.au
Linked In: au.linkedin.com/in/janetcolbyhra/
Look and feel

```html
<!DOCTYPE html>
<html lang="en">
<head>
<meta charset="utf-8">
<title>Harbor Ridge Advisory – Business Card Options</title>
<link href="https://fonts.googleapis.com/css2?family=Cormorant+Garamond:wght@500;600&family=Jost:wght@300;400&family=Satisfy&display=swap" rel="stylesheet">
<style>
  :root {
    --paper: #ffffff;
    --ink: #3a3a3a;
    --ink-soft: #555555;
    --brand-blue: #2f5fa8;
    --logo-grey: #6b6b6b;
    --card-grey: #9d9d9c;
    --band-grey: #7a7a7a;
    --outline: #1e1e1e;
    --on-grey: #f1f1f1;
    --watermark: rgba(255,255,255,0.55);
  }
  * { box-sizing: border-box; margin: 0; padding: 0; }
  html, body { width: 862px; height: 1200px; overflow: hidden; background: var(--paper); }
  body { position: relative; font-family: "Jost", "Futura", sans-serif; color: var(--ink); }

  .card { position: absolute; overflow: hidden; }
  .card--front { background: var(--paper); }
  .card--outlined { border: 2px solid var(--outline); }
  .card--back { background: var(--card-grey); color: var(--on-grey); }
  .card--portrait { width: 260px; height: 425px; }
  .card--landscape { width: 427px; height: 261px; }

  .band { position: absolute; left: 0; right: 0; background: var(--band-grey); }

  .logo-box {
    position: absolute; width: 79px; height: 71px; background: var(--logo-grey);
    color: #fff; font: 400 13px "Jost", sans-serif;
    display: flex; align-items: center; justify-content: center; letter-spacing: 0.02em;
  }

  .company {
    position: absolute; font-family: "Cormorant Garamond", "Times New Roman", serif;
    font-weight: 600; font-variant: small-caps; font-size: 16px; letter-spacing: 0.06em;
    color: #222; white-space: nowrap;
  }
  .person {
    position: absolute; font-family: "Satisfy", cursive; font-size: 18px;
    color: var(--brand-blue); white-space: nowrap;
  }
  .role { position: absolute; font-size: 12px; font-weight: 300; color: var(--ink-soft); white-space: nowrap; }

  .contacts { position: absolute; list-style: none; font-size: 10.4px; font-weight: 300; line-height: 16px; white-space: nowrap; }
  .contacts .email { font-size: 9.4px; }
  .centered { left: 0; right: 0; text-align: center; }

  .watermark {
    position: absolute; font-family: "Cormorant Garamond", serif; font-weight: 500;
    font-variant: small-caps; font-size: 22px; letter-spacing: 0.08em;
    color: var(--watermark); white-space: nowrap; transform-origin: center;
  }
</style>
</head>
<body>

  <!-- Portrait front, left-aligned contacts -->
  <section class="card card--front card--outlined card--portrait" style="left:90px; top:3px;">
    <div class="logo-box" style="left:89px; top:52px;">LOGO</div>
    <p class="company centered" style="top:136px; text-align:center;">Harbor Ridge Advisory</p>
    <p class="person centered" style="top:204px; text-align:center;">Janet Colby FCA</p>
    <p class="role centered" style="top:231px; text-align:center;">Principal Consultant</p>
    <ul class="contacts" style="left:24px; top:306px;">
      <li>Mobile:&nbsp; 0412 846 309</li>
      <li>Phone:&nbsp; 03 9871 2264</li>
      <li>P.O.Box 87, Larkfield VIC 3148</li>
      <li class="email">Email : janet@harborridgeadvisory.com.au</li>
      <li>www.harborridgeadvisory.com.au</li>
      <li>au.linkedin.com/in/janetcolbyhra</li>
    </ul>
    <div class="band" style="bottom:0; height:11px;"></div>
  </section>

  <!-- Portrait front, centred contacts -->
  <section class="card card--front card--outlined card--portrait" style="left:361px; top:1px;">
    <div class="logo-box" style="left:89px; top:51px;">LOGO</div>
    <p class="company centered" style="top:134px;">Harbor Ridge Advisory</p>
    <p class="person centered" style="top:203px;">Janet Colby FCA</p>
    <p class="role centered" style="top:230px;">Principal Consultant</p>
    <ul class="contacts centered" style="top:307px;">
      <li>Mobile:&nbsp; 0412 846 309</li>
      <li>Phone:&nbsp; 03 9871 2264</li>
      <li>P.O.Box 87, Larkfield VIC 3148</li>
      <li class="email">Email : janet@harborridgeadvisory.com.au</li>
      <li>www.harborridgeadvisory.com.au</li>
      <li>au.linkedin.com/in/janetcolbyhra</li>
    </ul>
    <div class="band" style="bottom:0; height:11px;"></div>
  </section>

  <!-- Portrait backs -->
  <section class="card card--back card--portrait" style="left:92px; top:438px;">
    <p class="watermark" style="left:-10px; top:165px; width:280px; text-align:center; transform:rotate(-52deg);">Harbor Ridge Advisory</p>
    <ul class="contacts centered" style="top:318px;">
      <li>Mobile:&nbsp; 0412 846 309</li>
      <li>Phone:&nbsp; 03 9871 2264</li>
      <li>P.O.Box 87, Larkfield VIC 3148</li>
      <li class="email">Email : janet@harborridgeadvisory.com.au</li>
      <li>www.harborridgeadvisory.com.au</li>
      <li>au.linkedin.com/in/janetcolbyhra</li>
    </ul>
  </section>

  <section class="card card--back card--portrait" style="left:359px; top:436px;">
    <p class="watermark" style="left:-10px; top:166px; width:280px; text-align:center; transform:rotate(-52deg);">Harbor Ridge Advisory</p>
    <ul class="contacts centered" style="top:319px;">
      <li>Mobile:&nbsp; 0412 846 309</li>
      <li>Phone:&nbsp; 03 9871 2264</li>
      <li>P.O.Box 87, Larkfield VIC 3148</li>
      <li class="email">Email : janet@harborridgeadvisory.com.au</li>
      <li>www.harborridgeadvisory.com.au</li>
      <li>au.linkedin.com/in/janetcolbyhra</li>
    </ul>
  </section>

  <!-- Landscape front -->
  <section class="card card--front card--landscape" style="left:0; top:937px; border:1px solid #8a8a8a;">
    <div class="band" style="top:0; height:9px;"></div>
    <p class="person" style="right:28px; top:24px;">Janet Colby FCA</p>
    <p class="role" style="right:45px; top:52px;">Principal Consultant</p>
    <div class="logo-box" style="left:47px; top:77px;">LOGO</div>
    <p class="company" style="left:177px; top:115px; color:var(--brand-blue);">Harbor Ridge Advisory</p>
    <svg style="position:absolute; left:177px; top:133px;" width="220" height="3" aria-hidden="true">
      <line x1="0" y1="1.5" x2="220" y2="1.5" stroke="var(--brand-blue)" stroke-width="1.5"/>
    </svg>
    <ul class="contacts" style="left:177px; top:141px;">
      <li>Mobile:&nbsp; 0412 846 309</li>
      <li>Phone:&nbsp; 03 9871 2264</li>
      <li>P.O.Box 87, Larkfield VIC 3148</li>
      <li class="email">Email : janet@harborridgeadvisory.com.au</li>
      <li>www.harborridgeadvisory.com.au</li>
      <li>au.linkedin.com/in/janetcolbyhra</li>
    </ul>
    <div class="band" style="bottom:0; height:10px;"></div>
  </section>

  <!-- Landscape back -->
  <section class="card card--back card--landscape" style="left:436px; top:937px; width:425px;">
    <p class="watermark" style="left:40px; top:92px; width:300px; text-align:center; transform:rotate(-20deg);">Harbor Ridge Advisory</p>
    <ul class="contacts" style="left:189px; top:152px;">
      <li>Mobile:&nbsp; 0412 846 309</li>
      <li>Phone:&nbsp; 03 9871 2264</li>
      <li>P.O.Box 87, Larkfield VIC 3148</li>
      <li class="email">Email : janet@harborridgeadvisory.com.au</li>
      <li>www.harborridgeadvisory.com.au</li>
      <li>au.linkedin.com/in/janetcolbyhra</li>
    </ul>
  </section>

</body>
</html>
```